Business Card & Letterhead Design

We a financial advice company based in Australia. We provide advice to wealthy farmers.

We are changing our business name FROM Palomar Financial TO Bluegate Wealth and we need a new letterhead and double sided business card design

Attached is designs from our previous branding (Palomar Financial) as it includes all the details we require on the new Bluegate Wealth business cards and letterhead.

```html
<!DOCTYPE html>
<html lang="en">
<head>
<meta charset="utf-8">
<title>Bluegate Wealth – Business Card</title>
<link rel="stylesheet" href="https://fonts.googleapis.com/css2?family=Cinzel:wght@400;500&family=Montserrat:wght@400;500&display=swap">
<style>
  :root{
    --backdrop:#2b2d2f;
    --slate:#5e6b71;
    --slate-light:#7d8c93;
    --charcoal:#47494b;
    --ink:#ffffff;
    --ink-soft:#e6eaec;
    --serif:'Cinzel', Georgia, serif;
    --sans:'Montserrat', Arial, sans-serif;
  }
  *{box-sizing:border-box;margin:0;padding:0}
  html,body{width:1200px;height:900px;overflow:hidden;background:var(--backdrop)}
  .canvas{position:relative;width:1200px;height:900px}
  .card{position:absolute;left:250px;width:700px;height:400px;border-radius:22px;overflow:hidden;background:var(--slate);color:var(--ink)}
  .card--front{top:35px}
  .card--back{top:465px}

  /* front */
  .front__brand{position:absolute;left:50px;top:62px;font-family:var(--serif);font-size:30px;letter-spacing:1px}
  .services{position:absolute;left:50px;top:122px;list-style:none}
  .services li{display:flex;align-items:center;gap:12px;font-family:var(--serif);font-size:19px;letter-spacing:.5px;margin-bottom:9px}
  .services svg{width:18px;height:18px;flex:none}
  .licensee{position:absolute;left:50px;top:292px;font-family:var(--sans);font-size:15px;line-height:1.55;color:var(--ink-soft)}
  .front__seal{position:absolute;right:60px;top:50px;width:200px;height:200px;border:4px solid var(--ink);border-radius:50%}

  /* back */
  .back__wave{position:absolute;inset:0;width:100%;height:100%}
  .back__brand{position:absolute;left:48px;top:58px;display:flex;align-items:center;gap:14px}
  .back__seal{width:58px;height:58px;border:3px solid var(--ink);border-radius:50%}
  .back__name{font-family:var(--serif);font-size:26px;letter-spacing:1px}
  .address{position:absolute;left:48px;top:150px;font-family:var(--sans);font-size:15px;line-height:1.6}
  .motto{position:absolute;left:48px;top:240px;font-family:var(--serif);font-size:18px;letter-spacing:.5px}
  .referral{position:absolute;left:48px;bottom:30px;font-family:var(--serif);font-size:17px;letter-spacing:1px}
  .person{position:absolute;right:40px;top:38px;text-align:right;font-family:var(--sans);font-size:14px;line-height:1.5;color:var(--ink-soft)}
  .person__name{font-family:var(--serif);font-size:20px;color:var(--ink)}
  .person__name span{font-family:var(--sans);font-size:14px;color:var(--ink-soft)}
  .contacts{position:absolute;right:36px;top:186px;list-style:none;text-align:right;font-family:var(--sans);font-size:14.5px;line-height:1.75}
  .contacts li{display:flex;justify-content:flex-end;align-items:center;gap:10px}
  .contacts svg{width:13px;height:13px;flex:none}
</style>
</head>
<body>
<main class="canvas">

  <section class="card card--front">
    <h1 class="front__brand">BLUEGATE WEALTH</h1>
    <ul class="services">
      <li><svg viewBox="0 0 18 18"><circle cx="9" cy="9" r="8" fill="none" stroke="#fff" stroke-width="1.4"/><rect x="5" y="9" width="2" height="4" fill="#fff"/><rect x="8" y="6" width="2" height="7" fill="#fff"/><rect x="11" y="8" width="2" height="5" fill="#fff"/></svg>LIFE &amp; TPD INSURANCE</li>
      <li><svg viewBox="0 0 18 18"><circle cx="9" cy="9" r="8" fill="none" stroke="#fff" stroke-width="1.4"/><rect x="5" y="9" width="2" height="4" fill="#fff"/><rect x="8" y="6" width="2" height="7" fill="#fff"/><rect x="11" y="8" width="2" height="5" fill="#fff"/></svg>INCOME PROTECTION</li>
      <li><svg viewBox="0 0 18 18"><circle cx="9" cy="9" r="8" fill="none" stroke="#fff" stroke-width="1.4"/><rect x="5" y="9" width="2" height="4" fill="#fff"/><rect x="8" y="6" width="2" height="7" fill="#fff"/><rect x="11" y="8" width="2" height="5" fill="#fff"/></svg>FINANCIAL PLANNING</li>
      <li><svg viewBox="0 0 18 18"><circle cx="9" cy="9" r="8" fill="none" stroke="#fff" stroke-width="1.4"/><rect x="5" y="9" width="2" height="4" fill="#fff"/><rect x="8" y="6" width="2" height="7" fill="#fff"/><rect x="11" y="8" width="2" height="5" fill="#fff"/></svg>RETIREMENT PLANNING</li>
    </ul>
    <p class="licensee">Meridian Advice Group Limited<br>Australian Financial Services Licensee-License Number 518203</p>
    <div class="front__seal" aria-hidden="true"></div>
  </section>

  <section class="card card--back">
    <svg class="back__wave" viewBox="0 0 700 400" preserveAspectRatio="none" aria-hidden="true">
      <path d="M0 318 C 250 318 320 118 700 118 L700 400 L0 400 Z" fill="var(--slate-light)"/>
      <path d="M0 338 C 260 338 340 148 700 148 L700 400 L0 400 Z" fill="var(--charcoal)"/>
    </svg>

    <div class="back__brand">
      <div class="back__seal" aria-hidden="true"></div>
      <h2 class="back__name">BLUEGATE WEALTH</h2>
    </div>
    <p class="address">Suite 4C, 18 Carrow St<br>Riverside Point, QLD 4170<br>PO Box 3352, Eastvale</p>
    <p class="motto">‘FINANCIAL PEACE OF MIND’</p>
    <p class="referral">A REFERRAL BUILT BUSINESS</p>

    <div class="person">
      <p class="person__name">TOM HALE <span>| B.Ag.Ec. Dip F.P. CFP®</span></p>
      <p>Managing Director</p>
      <p>Authorised Representative</p>
    </div>

    <ul class="contacts">
      <li>0400 555 218<svg viewBox="0 0 13 13"><rect x="3.5" y="1" width="6" height="11" rx="1.2" fill="none" stroke="#aab3b7" stroke-width="1.2"/></svg></li>
      <li>(07) 5550 1294<svg viewBox="0 0 13 13"><path d="M2 4 Q6.5 0 11 4 L9.5 5.5 L8 4.5 L5 4.5 L3.5 5.5 Z M3 7 H10 V11 H3 Z" fill="#aab3b7"/></svg></li>
      <li>(07) 5550 7731<svg viewBox="0 0 13 13"><rect x="2" y="4" width="9" height="6" rx="1" fill="#aab3b7"/><rect x="4" y="1.5" width="5" height="3" fill="#aab3b7"/></svg></li>
      <li>tom@bluegatewealth.com.au<svg viewBox="0 0 13 13"><rect x="1.5" y="3" width="10" height="7" rx="1" fill="none" stroke="#aab3b7" stroke-width="1.2"/><path d="M1.5 3.5 L6.5 7 L11.5 3.5" fill="none" stroke="#aab3b7" stroke-width="1.2"/></svg></li>
      <li>www.bluegatewealth.com.au<svg viewBox="0 0 13 13"><circle cx="6.5" cy="6.5" r="5" fill="none" stroke="#aab3b7" stroke-width="1.2"/><path d="M1.5 6.5 H11.5 M6.5 1.5 Q3.5 6.5 6.5 11.5 Q9.5 6.5 6.5 1.5" fill="none" stroke="#aab3b7" stroke-width="1"/></svg></li>
    </ul>
  </section>

</main>
</body>
</html>
```